Verdant QUICK Repairs Business card

Harbison Motors is looking for a business card design for our detailing wing "Verdant QUICK Repairs"
The services offered are vehicle paintless dent repairs, vehicle detailing, scratch and bumper repairs & paint and alloy wheel repairs.
Ideally the card design should be sharp, neat and professional. We are not looking for a card with pictures of cars.
Our corporate colours are blues (as in the logo supplied) which may look good with water droplets in high res and perhaps one or two images leaking off the card. Dark blacks with electric blues perhaps.
Images may be of a spray gun (we use Carrowmist), a rotary polisher (Trevalo Orbix) or similar objects used in the processes.

Industry/Entity Type

Paint

Contact Information for Business Card

Title: Verdant QUICK Repairs
Services: Bumper Repairs
Scratch/Paint Repairs
Paintless dent repairs
Alloy wheel repairs
Name: Martin K
Telephone: 0427195063
Email : martin@harbisonmotors.com.au

Font styles to use
Sans Serif
Other font styles liked:

Colors
0355a3
3277b5
0792cd
cfdfed

Requirements
Must have
• The title - "Verdant QUICK Repairs" should be a focus on either the from or back of the card
Should not have
• Photographs of cars

```html
<!DOCTYPE html>
<html lang="en">
<head>
<meta charset="utf-8">
<title>Verdant QUICK Repairs – Business Card</title>
<link rel="stylesheet" href="https://fonts.googleapis.com/css2?family=Fira+Sans:wght@300;400;500;700&display=swap">
<style>
  :root {
    --blue-deep: #0355a3;
    --blue-mid: #3277b5;
    --blue-electric: #0792cd;
    --blue-pale: #cfdfed;
    --navy: #14235e;
    --black: #1b1b1c;
    --white: #ffffff;
    --rule: #5a5a5c;
    --backdrop: #e9ecef;
  }
  * { box-sizing: border-box; margin: 0; padding: 0; }
  html, body {
    width: 1200px; height: 1000px; overflow: hidden;
    background: var(--backdrop);
    font-family: "Fira Sans", Arial, sans-serif;
  }
  .sheet {
    width: 1200px; height: 1000px;
    display: flex; flex-direction: column; align-items: center; justify-content: center;
    gap: 44px;
  }
  .card {
    position: relative; width: 760px; height: 434px; overflow: hidden;
    box-shadow: 0 6px 22px rgba(0,0,0,.18);
  }

  /* Front */
  .card-front { background: var(--black); }
  .card-front .corner { position: absolute; inset: 0; }
  .brand-box {
    position: absolute; left: 44px; top: 40px; width: 210px; height: 110px;
    background: var(--white);
    display: flex; align-items: center; justify-content: center; gap: 10px;
  }
  .brand-box .dot { width: 14px; height: 14px; border-radius: 50%; background: var(--blue-deep); }
  .brand-name { font-weight: 700; font-size: 20px; color: var(--navy); letter-spacing: .02em; }
  .divider { position: absolute; left: 44px; top: 172px; width: 330px; height: 1px; background: var(--rule); }
  .title {
    position: absolute; left: 44px; top: 196px;
    color: var(--white); font-weight: 500; font-size: 40px; letter-spacing: .01em;
  }
  .services {
    position: absolute; left: 46px; top: 258px; list-style: none;
    color: var(--white); font-weight: 300; font-size: 19px; line-height: 1.3;
  }

  /* Back */
  .card-back { background: var(--blue-deep); }
  .texture {
    position: absolute; inset: 0;
    background: radial-gradient(ellipse at 35% 45%, var(--blue-mid) 0%, var(--blue-deep) 70%);
  }
  .contact { position: absolute; left: 56px; top: 44px; color: var(--white); }
  .person { font-weight: 700; font-size: 44px; letter-spacing: .03em; margin-bottom: 12px; }
  .line { display: flex; align-items: center; gap: 14px; font-weight: 300; font-size: 22px; line-height: 1.5; }
  .line svg { width: 20px; height: 20px; flex: none; }
  .card-back .wedge { position: absolute; inset: 0; }
  .back-brand {
    position: absolute; right: 48px; bottom: 58px;
    display: flex; align-items: center; gap: 12px;
  }
  .back-brand .dot { width: 18px; height: 18px; border-radius: 50%; background: var(--blue-deep); }
  .back-brand .brand-name { font-size: 30px; }
</style>
</head>
<body>
<main class="sheet">

  <section class="card card-front" aria-label="Card front">
    <svg class="corner" viewBox="0 0 760 434" aria-hidden="true">
      <path d="M470 0 H760 V190 C720 80 620 18 470 0 Z" fill="var(--blue-deep)"/>
    </svg>
    <div class="brand-box"><span class="dot"></span><span class="brand-name">Harbison Motors</span></div>
    <div class="divider"></div>
    <h1 class="title">Verdant QUICK Repairs</h1>
    <ul class="services">
      <li>Bumper Repairs Scratch/Paint Repairs</li>
      <li>Paintless dent repairs</li>
      <li>Alloy wheel repairs</li>
    </ul>
  </section>

  <section class="card card-back" aria-label="Card back">
    <div class="texture" role="img" aria-label="Soft pattern of water droplets in blue tones"></div>
    <svg class="wedge" viewBox="0 0 760 434" aria-hidden="true">
      <polygon points="760,110 760,434 330,434" fill="var(--white)"/>
    </svg>
    <div class="contact">
      <p class="person">MARTIN K</p>
      <p class="line">
        <svg viewBox="0 0 24 24" aria-hidden="true"><path d="M6.6 10.8a15 15 0 0 0 6.6 6.6l2.2-2.2a1 1 0 0 1 1-.25 11.4 11.4 0 0 0 3.6.57 1 1 0 0 1 1 1V20a1 1 0 0 1-1 1A17 17 0 0 1 3 4a1 1 0 0 1 1-1h3.5a1 1 0 0 1 1 1c0 1.25.2 2.45.57 3.57a1 1 0 0 1-.25 1z" fill="var(--white)"/></svg>
        0427195063
      </p>
      <p class="line">
        <svg viewBox="0 0 24 24" aria-hidden="true"><rect x="2" y="5" width="20" height="14" fill="var(--white)"/><path d="M2 5l10 8 10-8" fill="none" stroke="var(--blue-deep)" stroke-width="1.6"/></svg>
        martin@harbisonmotors.com.au
      </p>
    </div>
    <div class="back-brand"><span class="dot"></span><span class="brand-name">Harbison Motors</span></div>
  </section>

</main>
</body>
</html>
```